Flyer Design for Earthworks Business in Australia

Gully Crest Earthworks is a new Earthworks and mini excavator business in Australia that requires an attention grabbing flyer to be used in our promotional material.

It will be dual sided and will be used for print media and also digital marketing. It will incorporate our logo, contact details and a list of our services offered.

Target Market(s)

Prospective clients that require earthworks

Industry/Entity Type

Construction and Earthworks

Requirements
Must have
• Must be dual sided, include our logo and contact information (phone number and Web page) and our services offered.
Nice to have
• QR link for Web site. Some photo(s) incorporated into the design.

```html
<!DOCTYPE html>
<html lang="en">
<head>
<meta charset="utf-8">
<title>Gully Crest Earthworks – Flyer</title>
<link href="https://fonts.googleapis.com/css2?family=Poppins:wght@500;600;700;800&family=Figtree:wght@400;500;600;700&display=swap" rel="stylesheet">
<style>
:root{
  --green:#c8d400;
  --slate:#343b3e;
  --ink:#262a2b;
  --footer:#2a2b2b;
  --paper:#ffffff;
  --stage:#e4e4e4;
  --text:#1d1d1d;
}
*{box-sizing:border-box;margin:0;padding:0}
html,body{width:1200px;height:908px;overflow:hidden;background:var(--stage)}
body{position:relative;font-family:"Figtree",sans-serif;color:var(--text)}
.card{position:absolute;top:52px;width:525px;height:743px;background:var(--paper);overflow:hidden}
.front{left:75px}
.back{left:632px}
.layer{position:absolute;left:0;top:0}

/* wordmark */
.wordmark{position:absolute;left:0;width:100%;text-align:center;font-family:"Poppins",sans-serif}
.wordmark .name{font-weight:700;font-size:32px;letter-spacing:2px;line-height:1}
.wordmark .tag{display:flex;align-items:center;justify-content:center;gap:8px;margin-top:6px;font-weight:600;font-size:10.5px;letter-spacing:4px}
.wordmark .tag::before,.wordmark .tag::after{content:"";display:block;width:56px;height:2px;background:currentColor}
.front .wordmark{top:100px;color:var(--ink)}
.back .wordmark{top:96px;color:#fff}
.mark-square{position:absolute;width:46px;height:46px;background:var(--green);left:50%;transform:translateX(-50%)}

/* front */
.headline{position:absolute;left:100px;top:214px;transform:rotate(-6.5deg);transform-origin:left top;
  font-family:"Poppins",sans-serif;font-weight:800;font-size:29px;line-height:1.3;color:#fff;letter-spacing:.5px}
.band-name{position:absolute;left:228px;top:318px;transform:rotate(-6deg);font-family:"Poppins",sans-serif;font-weight:700;font-size:15px;color:var(--green);letter-spacing:1px}
.support{position:absolute;left:40px;top:660px;font-family:"Poppins",sans-serif;color:var(--ink)}
.support .s1{font-weight:500;font-size:17px;line-height:1}
.support .s2{font-weight:800;font-size:35px;line-height:1.05}
.front-contact{position:absolute;left:246px;top:644px;color:#fff;font-family:"Poppins",sans-serif}
.front-contact .loc{font-size:17px;font-weight:500}
.front-contact .phone{font-size:24px;font-weight:700;margin-top:6px}
.front-contact .web{font-size:18px;font-weight:500;margin-top:6px}
.front-contact .web span{color:var(--green);font-weight:400}

/* back */
.why{position:absolute;top:180px;width:100%;text-align:center;font-family:"Poppins",sans-serif;font-weight:600;font-size:20.5px;letter-spacing:.8px;color:var(--slate)}
.photo{position:absolute;top:223px;height:134px;border:3px solid var(--green);border-radius:6px 6px 0 0}
.qualities{position:absolute;top:374px;left:0;width:100%;display:flex;justify-content:space-around;padding:0 40px 0 60px;font-size:13.5px;color:var(--slate)}
.qualities li{list-style:disc}
.service{position:absolute;display:flex;align-items:center;gap:14px;font-family:"Poppins",sans-serif;font-weight:600;font-size:14px;line-height:1.3;color:var(--ink)}
.service svg{flex:none}
.back-footer{position:absolute;left:0;top:635px;width:100%;height:108px;background:var(--footer);color:#fff;font-family:"Poppins",sans-serif}
.back-footer .firm{position:absolute;left:25px;top:25px;font-weight:600;font-size:16px;color:var(--green)}
.back-footer .dot{position:absolute;left:92px;top:56px;width:22px;height:22px;background:var(--green)}
.back-footer .lines{position:absolute;left:267px;top:22px;font-size:15px;line-height:23px}
.back-footer .lines b{color:var(--green);font-weight:600}

.label{position:absolute;top:836px;font-family:"Poppins",sans-serif;font-weight:700;font-size:28px;color:#111}
</style>
</head>
<body>

<section class="card front">
  <svg class="layer" width="525" height="743" viewBox="0 0 525 743">
    <defs>
      <linearGradient id="siteScene" x1="0" y1="0" x2="0" y2="1">
        <stop offset="0" stop-color="#8fb3d8"/>
        <stop offset=".35" stop-color="#cfdbe4"/>
        <stop offset=".45" stop-color="#5f7a4a"/>
        <stop offset=".6" stop-color="#8ba35c"/>
        <stop offset="1" stop-color="#6f8e3f"/>
      </linearGradient>
    </defs>
    <polygon points="0,173 470,158 525,150 0,197" fill="var(--green)"/>
    <polygon points="0,197 525,150 525,308 0,412" fill="var(--slate)"/>
    <polygon points="0,412 525,308 525,633 0,633" fill="url(#siteScene)" role="img" aria-label="Photo of a yellow mini excavator parked on a grassy site under a blue sky"/>
    <rect x="0" y="633" width="525" height="110" fill="var(--footer)"/>
    <polygon points="0,633 155,633 210,743 0,743" fill="var(--green)"/>
  </svg>
  <div class="mark-square" style="top:30px"></div>
  <div class="wordmark"><div class="name">GULLY CREST</div><div class="tag">EARTHWORKS</div></div>
  <div class="headline">NEED EARTHWORKS ?<br>WE’RE READY TO DIG</div>
  <div class="band-name">GULLY CREST</div>
  <div class="support"><div class="s1">SUPPORT</div><div class="s2">24/7</div></div>
  <div class="front-contact">
    <div class="loc">Ridgevale, Western Australia</div>
    <div class="phone">Ph: 0412 586 330</div>
    <div class="web"><span>Web:</span> gullycrest.com.au</div>
  </div>
</section>

<section class="card back">
  <svg class="layer" width="525" height="743" viewBox="0 0 525 743">
    <rect x="0" y="0" width="525" height="141" fill="var(--slate)"/>
    <rect x="0" y="141" width="525" height="6" fill="var(--green)"/>
    <rect x="0" y="292" width="525" height="112" fill="var(--green)"/>
    <rect x="0" y="629" width="525" height="6" fill="var(--green)"/>
  </svg>
  <div class="mark-square" style="top:22px"></div>
  <div class="wordmark"><div class="name">GULLY CREST</div><div class="tag">EARTHWORKS</div></div>
  <div class="why">WHY CHOOSE GULLY CREST</div>

  <div class="photo" style="left:15px;width:185px;background:linear-gradient(160deg,#8fa560,#7a6a4a 60%,#6b8a45)" role="img" aria-label="Photo of a freshly dug trench across a grassy field"></div>
  <div class="photo" style="left:200px;width:132px;background:linear-gradient(180deg,#a9c3df,#d8e1e6 35%,#7d9a55 55%,#6e7d47)" role="img" aria-label="Photo of an excavator beside a long trench line"></div>
  <div class="photo" style="left:332px;width:180px;background:linear-gradient(180deg,#9fbad6,#5d7a45 45%,#b9a585 75%,#a89272)" role="img" aria-label="Photo of a white tipper truck and machinery on site"></div>

  <ul class="qualities"><li>Local Focus</li><li>Fully Insured</li><li>Reliable</li><li>Skilled</li></ul>

  <div class="service" style="left:32px;top:438px">
    <svg width="40" height="46" viewBox="0 0 40 46"><path d="M20 2 C14 12 12 16 12 19 a8 8 0 0 0 16 0 C28 16 26 12 20 2Z" fill="#35a8e0"/><path d="M2 32h36M2 38h36M2 44h36" stroke="#9bb53a" stroke-width="3"/></svg>
    <span>Drainage &amp;<br>Earthmoving Support</span>
  </div>
  <div class="service" style="left:32px;top:512px">
    <svg width="40" height="34" viewBox="0 0 40 34"><line x1="6" y1="6" x2="34" y2="28" stroke="#333" stroke-width="7" stroke-linecap="round"/><line x1="6" y1="6" x2="34" y2="28" stroke="#888" stroke-width="3" stroke-linecap="round"/></svg>
    <span>Trenching</span>
  </div>
  <div class="service" style="left:32px;top:565px">
    <svg width="40" height="44" viewBox="0 0 40 44"><path d="M10 22 V10" stroke="#6a9a2a" stroke-width="2"/><ellipse cx="10" cy="10" rx="6" ry="8" fill="#9bc53d"/><circle cx="32" cy="14" r="4" fill="#f2b020"/><rect x="2" y="28" width="36" height="6" fill="#c98b4a"/><rect x="2" y="34" width="36" height="8" fill="#7a4e2a"/></svg>
    <span>Excavation &amp;<br>Site Preparation</span>
  </div>
  <div class="service" style="left:313px;top:438px">
    <svg width="44" height="40" viewBox="0 0 44 40"><path d="M12 4v12M22 2v14M32 4v12" stroke="#333" stroke-width="2"/><polygon points="2,36 10,24 34,24 42,36" fill="#e9b66a" stroke="#333" stroke-width="1.5"/></svg>
    <span>Pad and Slab<br>Preparation</span>
  </div>
  <div class="service" style="left:313px;top:512px">
    <svg width="44" height="40" viewBox="0 0 44 40"><path d="M4 4v34h38" stroke="#333" stroke-width="2" fill="none"/><rect x="8" y="16" width="8" height="20" fill="#333"/><rect x="18" y="8" width="8" height="28" fill="#3c5fa8"/><rect x="28" y="18" width="8" height="18" fill="#333"/></svg>
    <span>Footings &amp;<br>Foundations</span>
  </div>
  <div class="service" style="left:313px;top:568px">
    <svg width="44" height="44" viewBox="0 0 44 44"><rect x="14" y="18" width="16" height="14" fill="#c8d400" stroke="#333" stroke-width="1.5"/><path d="M14 22 L6 8 L2 22" stroke="#333" stroke-width="3" fill="none"/><rect x="10" y="34" width="26" height="7" rx="3.5" fill="#555"/></svg>
    <span>Machine Hire<br>with Operator</span>
  </div>

  <footer class="back-footer">
    <div class="firm">Gully Crest Earthworks</div>
    <div class="dot"></div>
    <div class="lines">
      <div><b>Ph:</b> 041 258 633</div>
      <div><b>Web:</b> gullycrest.com.au</div>
      <div><b>Email:</b> info@gullycrest.com.au</div>
    </div>
  </footer>
</section>

<div class="label" style="left:264px">Front</div>
<div class="label" style="left:858px">Back</div>

</body>
</html>
```